Cannabis Security Company- Sales Flyer

Take the copy and make a sleek design- no cannabis leave or paraphernalia. Add graphic elements to the Product Offering section

```html
<!DOCTYPE html>
<html lang="en">
<head>
<meta charset="utf-8">
<title>Vantage – Surveillance & IT Hardware Flyer</title>
<link href="https://fonts.googleapis.com/css2?family=Montserrat:wght@400;600;700;800&family=Open+Sans:wght@400;600;700&display=swap" rel="stylesheet">
<style>
:root{
  --slate:#36414f;
  --slate-dark:#262f3a;
  --blue:#4b93cc;
  --blue-light:#8fc1e6;
  --paper:#ffffff;
  --mist:#e6e9ec;
  --band:#c9ced4;
  --text:#3c4653;
}
*{margin:0;padding:0;box-sizing:border-box}
html,body{width:878px;height:1200px;overflow:hidden;background:var(--paper)}
.flyer{position:relative;width:878px;height:1200px;background:var(--paper);font-family:"Open Sans",Arial,sans-serif;color:var(--text)}
.service-mosaic{position:absolute;left:300px;top:0;width:578px;height:540px}
.service-label{font-family:"Montserrat",Arial,sans-serif;font-weight:700;font-size:13px;fill:#fff;letter-spacing:.5px}
.brand{position:absolute;left:40px;top:62px;display:flex;align-items:center;gap:14px;z-index:2}
.brand-mark{width:22px;height:22px;background:var(--slate)}
.brand-name{font-family:"Montserrat",Arial,sans-serif;font-weight:800;font-size:64px;letter-spacing:4px;color:var(--slate);line-height:1}
.headline{position:absolute;left:40px;top:290px;font-family:"Montserrat",Arial,sans-serif;font-weight:800;font-size:42px;line-height:50px;color:var(--slate);text-transform:uppercase;white-space:nowrap;z-index:2}
.intro{position:absolute;left:40px;top:528px;width:800px;font-size:13px;line-height:18px;text-align:center}
.offer-title{position:absolute;left:40px;top:622px;width:798px;display:flex;align-items:center;gap:16px;font-family:"Montserrat",Arial,sans-serif;font-weight:800;font-size:22px;color:var(--blue);white-space:nowrap}
.offer-title::before,.offer-title::after{content:"";flex:1;height:2px;background:var(--blue)}
.benefits{position:absolute;left:60px;top:660px;width:780px;list-style:none;font-size:12.5px;line-height:17px}
.benefits li{padding-left:12px;position:relative;margin-bottom:3px}
.benefits li::before{content:"";position:absolute;left:0;top:6px;width:5px;height:5px;background:var(--blue)}
.benefits b{color:var(--blue);font-weight:700;text-transform:uppercase}
.finance{list-style:none;margin:3px 0 0 24px}
.finance li::before{background:var(--slate);width:4px;height:4px}
.finance b{color:var(--text);text-transform:none}
.product-band{position:absolute;left:0;top:888px;width:878px;height:78px;background:var(--band);display:flex;align-items:center;justify-content:center}
.product-title{font-family:"Montserrat",Arial,sans-serif;font-weight:800;font-size:52px;letter-spacing:6px;color:#fff;opacity:.9}
.products{position:absolute;left:0;top:966px;width:878px;height:112px;background:var(--slate);display:flex;justify-content:space-around;align-items:center;padding:0 30px}
.product{display:flex;align-items:center;gap:10px;color:#fff;font-family:"Montserrat",Arial,sans-serif;font-weight:700;font-size:12px;line-height:15px;text-transform:uppercase}
.product svg{flex:none}
.cta{position:absolute;left:0;top:1078px;width:878px;height:88px;background:var(--blue);color:#fff;text-align:center}
.cta-title{font-family:"Montserrat",Arial,sans-serif;font-weight:800;font-size:22px;padding-top:12px;letter-spacing:.5px}
.contacts{display:flex;justify-content:center;gap:46px;margin-top:10px;font-size:14px;font-weight:600}
.contacts span{display:flex;align-items:center;gap:7px}
.footer-strip{position:absolute;left:0;top:1166px;width:878px;height:34px;background:var(--mist)}
</style>
</head>
<body>
<div class="flyer">

  <svg class="service-mosaic" viewBox="300 0 578 540">
    <defs>
      <linearGradient id="tone-slate" x1="0" y1="0" x2="1" y2="1"><stop offset="0" stop-color="#4d5b6c"/><stop offset="1" stop-color="#222a34"/></linearGradient>
      <linearGradient id="tone-blue" x1="0" y1="0" x2="1" y2="1"><stop offset="0" stop-color="#6aa9d8"/><stop offset="1" stop-color="#2c4f72"/></linearGradient>
      <linearGradient id="tone-steel" x1="0" y1="1" x2="1" y2="0"><stop offset="0" stop-color="#5c6f82"/><stop offset="1" stop-color="#a9bccb"/></linearGradient>
      <linearGradient id="tone-night" x1="0" y1="0" x2="1" y2="1"><stop offset="0" stop-color="#3b5672"/><stop offset="1" stop-color="#161d26"/></linearGradient>
    </defs>
    <polygon points="540,0 580,40 540,80 500,40" fill="#3a4553"/>
    <polygon points="660,5 755,100 660,195 565,100" fill="url(#tone-steel)" role="img" aria-label="Photo of an installation technician at a server rack"/>
    <polygon points="484,150 584,250 484,350 384,250" fill="url(#tone-blue)" role="img" aria-label="Photo of a shipping port with cargo containers"/>
    <polygon points="770,155 860,245 770,335 680,245" fill="url(#tone-night)" role="img" aria-label="Photo of a professional at a desk with monitors"/>
    <polygon points="620,275 705,360 620,445 535,360" fill="url(#tone-slate)" role="img" aria-label="Photo of a media control room"/>
    <polygon points="850,390 905,445 850,500 795,445" fill="#c9ced4"/>
    <text class="service-label" x="660" y="96" text-anchor="middle">FULL SERVICE</text>
    <text class="service-label" x="660" y="112" text-anchor="middle">INTEGRATION</text>
    <text class="service-label" x="484" y="246" text-anchor="middle">GLOBAL SOURCING</text>
    <text class="service-label" x="484" y="262" text-anchor="middle">SPECIALISTS</text>
    <text class="service-label" x="770" y="241" text-anchor="middle">PROFESSIONAL</text>
    <text class="service-label" x="770" y="257" text-anchor="middle">SERVICES</text>
    <text class="service-label" x="620" y="356" text-anchor="middle">MEDIA &amp;</text>
    <text class="service-label" x="620" y="372" text-anchor="middle">ENTERTAINMENT</text>
  </svg>

  <div class="brand"><span class="brand-mark"></span><span class="brand-name">VANTAGE</span></div>

  <h1 class="headline">Let Vantage<br>take care of<br>your surveillance<br>and IT hardware needs</h1>

  <p class="intro">Due to the regulations put forth by the State of California, there is high cost associated with being in compliance to maintain your license and not receive fines as it pertains to security for your facility. In addition, the data intense programs with the seed-to-sale program can be a hindrance to you doing what you do best: running your business!</p>

  <h2 class="offer-title">WHAT VANTAGE CAN OFFER</h2>

  <ul class="benefits">
    <li><b>Experience</b>- we have been in the IT and video surveillance business for over 20 years</li>
    <li><b>Compliance</b>- our attorney helped write Prop 64 and can keep you in compliance with the ever-changing regulations</li>
    <li><b>Cost savings</b>- Vantage can save you 15-30% over the competition</li>
    <li><b>Speed</b>- our solutions can be designed and implemented within days, not months</li>
    <li><b>Customization</b>- our products are architected around the business not the business around the product</li>
    <li><b>Finance options</b>- Vantage offers the following options for purchase
      <ul class="finance">
        <li><b>Outright purchase</b>- own your own equipment and data</li>
        <li><b>Leasing with a monthly payment</b>- prevent large outlay of cash</li>
        <li><b>Managed/cloud offering</b>- we send the gear and manage in a secure location</li>
      </ul>
    </li>
  </ul>

  <div class="product-band"><span class="product-title">PRODUCT OFFERING</span></div>

  <div class="products">
    <div class="product">
      <svg width="46" height="46" viewBox="0 0 46 46"><circle cx="23" cy="23" r="22" fill="var(--blue)"/><rect x="11" y="17" width="17" height="12" rx="2" fill="#fff"/><polygon points="28,21 35,17 35,29 28,25" fill="#fff"/></svg>
      <span>Video<br>Surveillance</span>
    </div>
    <div class="product">
      <svg width="46" height="46" viewBox="0 0 46 46"><circle cx="23" cy="23" r="22" fill="var(--blue)"/><ellipse cx="23" cy="14" rx="9" ry="3.5" fill="#fff"/><path d="M14 17v5c0 2 4 3.5 9 3.5s9-1.5 9-3.5v-5c0 2-4 3.5-9 3.5s-9-1.5-9-3.5zM14 25v6c0 2 4 3.5 9 3.5s9-1.5 9-3.5v-6c0 2-4 3.5-9 3.5s-9-1.5-9-3.5z" fill="#fff"/></svg>
      <span>Data<br>Storage</span>
    </div>
    <div class="product">
      <svg width="46" height="46" viewBox="0 0 46 46"><circle cx="23" cy="23" r="22" fill="var(--blue)"/><path d="M17 21v-4a6 6 0 0 1 12 0v4" stroke="#fff" stroke-width="3" fill="none"/><rect x="14" y="21" width="18" height="13" rx="2" fill="#fff"/></svg>
      <span>Data<br>Security</span>
    </div>
    <div class="product">
      <svg width="46" height="46" viewBox="0 0 46 46"><circle cx="23" cy="23" r="22" fill="var(--blue)"/><g stroke="#fff" stroke-width="2"><line x1="23" y1="23" x2="23" y2="11"/><line x1="23" y1="23" x2="12" y2="30"/><line x1="23" y1="23" x2="34" y2="30"/></g><g fill="#fff"><circle cx="23" cy="23" r="4"/><circle cx="23" cy="11" r="3"/><circle cx="12" cy="30" r="3"/><circle cx="34" cy="30" r="3"/></g></svg>
      <span>Networking</span>
    </div>
    <div class="product">
      <svg width="46" height="46" viewBox="0 0 46 46"><circle cx="23" cy="23" r="22" fill="var(--blue)"/><g stroke="#fff" stroke-width="3" fill="none" stroke-linecap="round"><path d="M11 20a17 17 0 0 1 24 0"/><path d="M15 25a11 11 0 0 1 16 0"/></g><circle cx="23" cy="31" r="3" fill="#fff"/></svg>
      <span>Wireless<br>Connectivity</span>
    </div>
  </div>

  <div class="cta">
    <div class="cta-title">CALL US TODAY FOR A FREE CONSULTATION</div>
    <div class="contacts">
      <span><svg width="14" height="14" viewBox="0 0 14 14"><circle cx="7" cy="7" r="6" fill="none" stroke="#fff" stroke-width="1.5"/><line x1="1" y1="7" x2="13" y2="7" stroke="#fff"/><ellipse cx="7" cy="7" rx="2.5" ry="6" fill="none" stroke="#fff"/></svg>www.vantagedistributing.com</span>
      <span><svg width="16" height="12" viewBox="0 0 16 12"><rect x="1" y="1" width="14" height="10" fill="none" stroke="#fff" stroke-width="1.5"/><path d="M1 1l7 6 7-6" fill="none" stroke="#fff" stroke-width="1.5"/></svg>info@vantagedistributing.com</span>
      <span><svg width="14" height="14" viewBox="0 0 14 14"><path d="M3 1l3 3-2 2a8 8 0 0 0 4 4l2-2 3 3-2 2C6 13 1 8 1 3z" fill="#fff"/></svg>555-010-7050</span>
    </div>
  </div>

  <div class="footer-strip"></div>
</div>
</body>
</html>
```